Staylume.com banner design

Staylume.com is looking for a designer to work with ongoing to create a variety of banners.

For this competition we are looking for entrants to create two flash banners with dimensions 300x250 and a static banner/jpg. Each flash banner has two separate concepts one with more copy and more required 'slides' and one with less. The copy for each banner is as follows:

Concept 1: - 4 slide flash banner/animated gif
Save up to 75% on 150,000 Hotels Worldwide.
10% of profits go to local charities.
Do something good when you travel.
End screen call to action - Book now @ staylume.com (click here)

Concept 1a: 3 slide flash banner/animated gif

Concept 2: 4 slide flash banner/animated gif
$0 Booking fees. Best price guarantee.

Concept 2a: 3 slide flash banner/animated gif

Concept 3 – Static Banner
Book now @ staylume.com (click here)

Concept 3a

We expect two different designs, one for Concept 1 and 1a and a different design for concept 2 and 2a. Concept 3 (the static banners) can adopt the design used for the flash banners.

We also expect a gif version of the flash banners to be delivered.

The winning entry will then be hired to create each banner in a variety of banner sizes.
Updates

Project Deadline Extended
Reason: We are not satisfied with the number of entries so are extending this competition. We are looking for a long term relationship with a quality designer to produce a whole range of banners and other designs for staylume.com.

Industry/Entity Type

Accommodation

Requirements
Must have
• The staylume.com logo must always be visible on all banners.

Maximum flash file size is 50k
Max Frame Rate 24fps

```html
<!DOCTYPE html>
<html lang="en">
<head>
<meta charset="utf-8">
<title>Staylume.com banner storyboards</title>
<link rel="stylesheet" href="https://fonts.googleapis.com/css2?family=Montserrat:wght@400;500;600;700&display=swap">
<style>
  :root {
    --page: #ffffff;
    --ink: #111111;
    --grey-text: #6a6a6a;
    --panel-border: #d8d8d8;
    --panel-white: #fbfbfb;
    --orange: #f39a1e;
    --orange-dark: #c97a10;
    --blue-top: #62b2e6;
    --blue-bottom: #3f8fcc;
    --blue-edge: #3a80b8;
    --sunset-top: #6f6497;
    --sunset-mid: #c07a98;
    --sunset-glow: #f6a06a;
    --sunset-sea: #4a3a45;
    --coast-sky: #c9cfc6;
    --coast-green: #3f5a1e;
    --coast-rock: #2e2418;
  }
  * { margin: 0; padding: 0; box-sizing: border-box; }
  html, body { width: 717px; height: 1200px; overflow: hidden; background: var(--page); }
  body { font-family: "Montserrat", Arial, sans-serif; color: var(--ink); }
  .stage { position: relative; width: 750px; height: 1255px; transform: scale(0.956); transform-origin: 0 0; }

  .column-title { position: absolute; top: 56px; width: 300px; text-align: center; }
  .column-title h2 { font-size: 16px; font-weight: 500; letter-spacing: 1.2px; }
  .column-title p { font-size: 11px; font-weight: 500; letter-spacing: 1px; margin-top: 8px; }

  .banner { position: absolute; width: 300px; height: 249px; border: 1px solid var(--panel-border); background: var(--panel-white); overflow: hidden; }
  .photo { position: absolute; left: 0; width: 100%; }
  .photo--sunset { background: linear-gradient(180deg, var(--sunset-top) 0%, var(--sunset-mid) 45%, var(--sunset-glow) 75%, var(--sunset-sea) 100%); }
  .photo--coast { background: linear-gradient(180deg, var(--coast-sky) 0%, var(--coast-sky) 35%, var(--coast-green) 60%, var(--coast-rock) 100%); }

  .brand { position: absolute; display: flex; align-items: center; gap: 5px; font-weight: 500; color: #222; white-space: nowrap; }
  .brand .dot { width: 0.95em; height: 0.95em; border-radius: 50%; background: var(--orange); flex: none; }

  .btn { position: absolute; display: flex; align-items: center; justify-content: center; gap: 5px; height: 26px; border-radius: 3px; border: 1px solid var(--blue-edge); background: linear-gradient(180deg, var(--blue-top), var(--blue-bottom)); color: #fff; font-size: 11px; font-weight: 600; letter-spacing: 0.6px; }
  .btn svg { width: 9px; height: 12px; }

  .overlay { position: absolute; left: 0; width: 100%; text-align: center; color: #fff; font-weight: 600; }
  .rule-row { display: flex; align-items: center; justify-content: center; gap: 10px; }
  .rule-row i { display: block; width: 75px; height: 1px; background: rgba(255,255,255,0.85); }
  .big-figure { font-size: 30px; font-weight: 700; line-height: 1; }

  .ribbon { position: absolute; left: 18px; top: 62px; width: 262px; height: 62px; }
  .ribbon-text { position: absolute; left: 0; top: 62px; width: 100%; height: 52px; display: flex; align-items: center; justify-content: center; text-align: center; color: #fff; font-size: 15px; font-weight: 600; line-height: 1.3; }

  .bottom-bar { position: absolute; left: 0; bottom: 0; width: 100%; height: 44px; background: var(--panel-white); }

  .orange-figure { color: var(--orange); font-weight: 700; line-height: 1; }
  .grey-copy { color: var(--grey-text); font-size: 14px; font-weight: 500; line-height: 1.3; }
  .orange-copy { color: var(--orange); font-weight: 600; text-align: center; }
  .grey-rule { position: absolute; height: 1px; background: #cfcfcf; }
</style>
</head>
<body>
<div class="stage">
  <svg width="0" height="0" style="position:absolute">
    <defs>
      <symbol id="pin" viewBox="0 0 9 12"><path d="M4.5 0A4.5 4.5 0 0 0 0 4.5C0 8 4.5 12 4.5 12S9 8 9 4.5A4.5 4.5 0 0 0 4.5 0Zm0 6.3a1.8 1.8 0 1 1 0-3.6 1.8 1.8 0 0 1 0 3.6Z" fill="#fff"/></symbol>
    </defs>
  </svg>

  <div class="column-title" style="left:55px"><h2>FLASH STORYBOARD</h2><p>CONCEPT 1</p></div>
  <div class="column-title" style="left:403px"><h2>FLASH STORYBOARD</h2><p>CONCEPT 2</p></div>

  <!-- Concept 1 -->
  <section class="banner" style="left:55px; top:121px">
    <div class="photo photo--sunset" style="top:0; height:205px" role="img" aria-label="Sunset over the sea with purple and orange sky"></div>
    <div class="overlay" style="top:58px">
      <p style="font-size:15px">Save up to</p>
      <div class="rule-row" style="margin-top:2px"><i></i><span class="big-figure">75%</span><i></i></div>
      <p style="font-size:14px; margin-top:3px">on 150,000 Hotels Worldwide.</p>
    </div>
    <div class="bottom-bar">
      <div class="brand" style="left:12px; top:13px; font-size:14px"><span class="dot"></span>Staylume.com</div>
      <div class="btn" style="left:184px; top:9px; width:105px"><svg><use href="#pin"/></svg>BOOK NOW</div>
    </div>
  </section>

  <section class="banner" style="left:55px; top:386px">
    <div class="photo photo--sunset" style="top:0; height:204px" role="img" aria-label="Sunset over the sea with purple and orange sky"></div>
    <div class="overlay" style="top:70px">
      <div class="rule-row"><i></i><span class="big-figure">10%</span><i></i></div>
      <p style="font-size:14px; margin-top:4px">of profits go to local charities.</p>
    </div>
    <div class="bottom-bar">
      <div class="brand" style="left:12px; top:13px; font-size:14px"><span class="dot"></span>Staylume.com</div>
      <div class="btn" style="left:184px; top:9px; width:105px"><svg><use href="#pin"/></svg>BOOK NOW</div>
    </div>
  </section>

  <section class="banner" style="left:55px; top:658px">
    <div class="photo photo--sunset" style="top:0; height:204px" role="img" aria-label="Sunset over the sea with purple and orange sky"></div>
    <svg class="ribbon" viewBox="0 0 262 62" aria-hidden="true">
      <polygon points="0,10 24,10 24,52 0,52 10,31" fill="var(--orange-dark)"/>
      <polygon points="262,10 238,10 238,52 262,52 252,31" fill="var(--orange-dark)"/>
      <rect x="20" y="0" width="222" height="52" fill="var(--orange)"/>
    </svg>
    <div class="ribbon-text">Do something good<br>when you travel.</div>
    <div class="bottom-bar">
      <div class="brand" style="left:12px; top:13px; font-size:14px"><span class="dot"></span>Staylume.com</div>
      <div class="btn" style="left:184px; top:9px; width:105px"><svg><use href="#pin"/></svg>BOOK NOW</div>
    </div>
  </section>

  <section class="banner" style="left:55px; top:926px">
    <div class="photo photo--sunset" style="top:0; height:128px" role="img" aria-label="Sunset over the sea with purple and orange sky"></div>
    <p style="position:absolute; top:148px; width:100%; text-align:center; font-size:14px; font-weight:500">Book now @</p>
    <div class="brand" style="left:50%; top:169px; transform:translateX(-50%); font-size:20px"><span class="dot"></span>Staylume.com</div>
    <div class="btn" style="left:101px; top:204px; width:106px">CLICK HERE</div>
  </section>

  <!-- Concept 2 -->
  <section class="banner" style="left:403px; top:121px">
    <div class="brand" style="left:14px; top:12px; font-size:13px"><span class="dot"></span>Staylume.com</div>
    <div class="orange-figure" style="position:absolute; left:14px; top:46px; font-size:44px">$0</div>
    <p class="grey-copy" style="position:absolute; left:76px; top:52px">Booking fees.<br>Best price guarantee.</p>
    <div class="photo photo--coast" style="top:109px; height:140px" role="img" aria-label="Coastal rock temple with green trees and walkers by the sea"></div>
    <div class="btn" style="left:184px; top:215px; width:105px"><svg><use href="#pin"/></svg>BOOK NOW</div>
  </section>

  <section class="banner" style="left:403px; top:386px">
    <div class="brand" style="left:14px; top:12px; font-size:13px"><span class="dot"></span>Staylume.com</div>
    <div class="orange-figure" style="position:absolute; left:14px; top:46px; font-size:44px">10<span style="font-size:22px; vertical-align:top">%</span></div>
    <p class="grey-copy" style="position:absolute; left:100px; top:51px">of profits go to<br>local charities.</p>
    <div class="photo photo--coast" style="top:108px; height:141px" role="img" aria-label="Coastal rock temple with green trees and walkers by the sea"></div>
    <div class="btn" style="left:184px; top:214px; width:105px"><svg><use href="#pin"/></svg>BOOK NOW</div>
  </section>

  <section class="banner" style="left:403px; top:648px">
    <div class="brand" style="left:50%; top:32px; transform:translateX(-50%); font-size:17px"><span class="dot"></span>Staylume.com</div>
    <div class="grey-rule" style="left:25px; top:116px; width:50px"></div>
    <div class="grey-rule" style="left:222px; top:116px; width:50px"></div>
    <p class="orange-copy" style="position:absolute; left:0; top:82px; width:100%; font-size:17px; line-height:1.35">Do something<br>good when<br>you travel.</p>
    <div class="photo photo--coast" style="top:172px; height:77px" role="img" aria-label="Coastal rock temple with green trees and walkers by the sea"></div>
    <div class="btn" style="left:184px; top:215px; width:105px"><svg><use href="#pin"/></svg>BOOK NOW</div>
  </section>

  <section class="banner" style="left:403px; top:910px">
    <p class="orange-copy" style="position:absolute; left:0; top:32px; width:100%; font-size:14px; font-weight:500">Book Now at</p>
    <div class="brand" style="left:50%; top:56px; transform:translateX(-50%); font-size:17px"><span class="dot"></span>Staylume.com</div>
    <div class="photo photo--coast" style="top:104px; height:145px" role="img" aria-label="Coastal rock temple with natural arch and walkers by the sea"></div>
    <div class="btn" style="left:97px; top:93px; width:106px"><svg><use href="#pin"/></svg>CLICK HERE</div>
  </section>
</div>
</body>
</html>
```